Business card for builder specialising in renovations.

Need a card for our building business. Business name is under Marcus Pellow.
Have licence number on card ( 527196K)
Contact number (0400 583 214)
Want to work on logo for some business cards and shirts - something with MP or MPB or open to ideas??
No animations, No hammers. Something sharp and eye catching.
Highlight that we are a renovation specialist. Simple on front with extra details on back with some lines to jot down things.

Target Market(s)

Renovators

Industry/Entity Type

Building

Contact Information for Business Card

2 sided with room on back to jot things down.
Extra details on back so front can be simple ..like, renovations, bathrooms, decks, extensions, new builds,

Logo Text

MP

Font styles to use
Serif

Requirements
Must have
• Eye catching design .
• Name : Marcus pellow
• Licence number
• Contact number - 0400583214
Nice to have
• Some logo design that we can carry through to other forms of advertising
• Local builder
• Quality work
Should not have
• No animations

```html
<!DOCTYPE html>
<html lang="en">
<head>
<meta charset="utf-8">
<title>Marcus Pellow – Business Card</title>
<link href="https://fonts.googleapis.com/css2?family=Crimson+Text:ital,wght@0,400;0,700;1,400&display=swap" rel="stylesheet">
<style>
  :root {
    --backdrop: #e4e5e7;
    --brand-blue: #0b8bc8;
    --brand-red: #dd3b40;
    --paper: #f7f7f5;
    --ink: #4a4a4a;
    --card-shadow: 0 10px 28px rgba(0, 0, 0, 0.18);
  }

  * { box-sizing: border-box; margin: 0; padding: 0; }

  html, body {
    width: 1200px;
    height: 960px;
    overflow: hidden;
  }

  body {
    background: var(--backdrop);
    font-family: "Crimson Text", Georgia, serif;
    display: flex;
    flex-direction: column;
    align-items: center;
    justify-content: center;
    gap: 40px;
  }

  .card {
    position: relative;
    width: 700px;
    height: 410px;
    box-shadow: var(--card-shadow);
    overflow: hidden;
  }

  /* Logo side */
  .card--logo {
    background: var(--brand-blue);
    display: flex;
    align-items: center;
    justify-content: center;
  }

  .wordmark {
    font-family: "Crimson Text", Georgia, serif;
    font-weight: 700;
    line-height: 1;
    letter-spacing: 0.04em;
  }

  .card--logo .wordmark {
    color: #ffffff;
    font-size: 150px;
  }

  /* Details side */
  .card--details {
    background: var(--paper);
    text-align: center;
  }

  .card--details .wordmark {
    position: absolute;
    top: 56px;
    left: 0;
    right: 0;
    color: var(--brand-blue);
    font-size: 100px;
  }

  .edge-tab {
    position: absolute;
    width: 44px;
    background: var(--brand-red);
  }

  .edge-tab--left {
    left: 0;
    top: 66px;
    height: 120px;
    clip-path: polygon(0 0, 40% 0, 100% 30%, 100% 70%, 40% 100%, 0 100%);
  }

  .edge-tab--right {
    right: 0;
    top: 196px;
    height: 130px;
    clip-path: polygon(60% 0, 100% 0, 100% 100%, 60% 100%, 0 75%, 0 25%);
  }

  .holder-name {
    position: absolute;
    top: 214px;
    left: 0;
    right: 0;
    color: var(--brand-red);
    font-weight: 700;
    font-size: 24px;
  }

  .contact-lines {
    position: absolute;
    top: 268px;
    left: 0;
    right: 0;
    list-style: none;
    color: var(--ink);
    font-style: italic;
    font-size: 19px;
    line-height: 1.45;
  }
</style>
</head>
<body>

  <section class="card card--logo" aria-label="Card back">
    <span class="wordmark">MP</span>
  </section>

  <section class="card card--details" aria-label="Card front">
    <span class="edge-tab edge-tab--left"></span>
    <span class="edge-tab edge-tab--right"></span>
    <span class="wordmark">MP</span>
    <h1 class="holder-name">Marcus pellow</h1>
    <ul class="contact-lines">
      <li>Contact number: 0400583214</li>
      <li>Licence number: 527196K</li>
    </ul>
  </section>

</body>
</html>
```